Price List Modified

We have a price list in PDF that we need changed. The current price list is in Euro's and we need the Euro's changed to U.S. dollars. We simply use a conversion factor of 1.55 for this.

We also need the dimensions of units converted from MM to inches.

Industry/Entity Type

Graphic Design

```html
<!DOCTYPE html>
<html lang="en">
<head>
<meta charset="utf-8">
<title>Regeneration and holding ovens – price list</title>
<link href="https://fonts.googleapis.com/css2?family=Roboto+Condensed:wght@300;400;700;900&display=swap" rel="stylesheet">
<style>
:root{
  --ink:#1d1d1b;
  --soft:#555;
  --rule:#9a9a9a;
  --accent:#f08a24;
  --steel:#c9c9c9;
  --paper:#fff;
}
*{box-sizing:border-box;margin:0;padding:0}
html,body{width:849px;height:1200px;overflow:hidden;background:var(--paper)}
body{position:relative;font-family:"Roboto Condensed",Arial,sans-serif;color:var(--ink)}
.page-head{position:absolute;left:48px;top:47px;font-size:13.5px;line-height:16px}
.page-head .it{font-weight:700}
.page-head .en{font-weight:400}
.elec-icon{position:absolute;left:48px;top:117px}
.section{position:absolute;left:228px;width:572px;height:460px}
.s-title{position:absolute;left:0;top:0;font-size:27px;line-height:26px;font-weight:400;letter-spacing:.2px}
.s-title b{font-weight:900}
.s-bar{position:absolute;left:0;top:27px;width:572px;height:5px;background:var(--accent)}
.hd{position:absolute;top:36px;font-size:9.5px;line-height:11px}
.hd span{display:block;color:var(--soft);font-weight:300}
.group{position:absolute;left:0;width:572px;height:72px;border-bottom:1px solid var(--rule);font-size:9px}
.group .sep{position:absolute;top:-2px;width:1px;height:72px;background:#bbb}
.code{position:absolute;left:4px;font-weight:700;font-size:11px}
.r1{top:12px}.r2{top:48px}
.code-rule{position:absolute;left:0;top:35px;width:64px;height:1px;background:#bbb}
.ver{position:absolute;left:66px;top:13px;font-size:9.5px;line-height:10.5px}
.ver span{color:var(--soft);font-weight:300}
.cap{position:absolute;left:158px;font-size:9px}
.cap b{font-size:13px;font-weight:700}
.step{position:absolute;left:231px;font-size:9.5px;display:flex;align-items:center;gap:6px}
.step.r1{top:6px}.step.r2{top:42px}
.mid{position:absolute;top:29px;font-size:9px}
.dims{left:300px}.wt{left:381px}.pw{left:426px}.price{left:519px;font-weight:700}
.note{position:absolute;left:0;font-size:9.5px;line-height:11px}
.note span{display:block;color:var(--soft);font-weight:300}
.acc{position:absolute;left:0;width:572px;height:31px;border-bottom:1px solid var(--rule);font-size:9px}
.acc .code{top:9px}
.acc .ver{top:4px}
.acc .mid{top:10px}
.photo{position:absolute;background:linear-gradient(180deg,#dedede,#b9b9b9 60%,#a7a7a7)}
.stand{position:absolute;background:linear-gradient(180deg,#f4f4f4,#e4e4e4)}
.caption{position:absolute;font-size:9.5px}
.foot-rule{position:absolute;left:48px;top:1152px;width:752px;height:1px;background:#f6d2aa}
.folio{position:absolute;left:784px;top:1167px;font-size:16px}
</style>
</head>
<body>
<header class="page-head">
  <div class="it">FORNI DI RIMESSA IN TEMPERATURA E MANTENIMENTO -18°C/+3°C &nbsp;⟶ +65°C</div>
  <div class="en">REGENERATION AND HOLDING OVENS &nbsp;-18°C/+3°C &nbsp;⟶ +65°C</div>
</header>

<svg class="elec-icon" width="20" height="16" viewBox="0 0 20 16" aria-hidden="true">
  <rect x="0" y="0" width="20" height="16" rx="2" fill="var(--ink)"/>
  <path d="M11 2 L6 9 H10 L8 14 L14 6 H10 Z" fill="#fff"/>
</svg>

<!-- Section 1 -->
<div class="photo" style="left:48px;top:200px;width:130px;height:128px" role="img" aria-label="Photo of the 062-072 electronic holding oven"></div>
<div class="caption" style="left:48px;top:331px">RTH 062-072 E</div>
<div class="stand" style="left:45px;top:512px;width:76px;height:98px" role="img" aria-label="Line drawing of the support base"></div>
<div class="caption" style="left:48px;top:613px">BSE 021</div>

<section class="section" style="top:113px">
  <h2 class="s-title"><b>RTH</b> 062 - 072</h2>
  <div class="s-bar"></div>
  <div class="hd" style="left:4px">Codice<span>Code</span></div>
  <div class="hd" style="left:66px">Versione<span>Version</span></div>
  <div class="hd" style="left:157px">Capacità<span>Capacity</span></div>
  <div class="hd" style="left:231px">Passo guide<span>Distance guides</span></div>
  <div class="hd" style="left:300px">Dimensioni inch<span>Dimensions inch</span></div>
  <div class="hd" style="left:381px">Peso<span>Weight</span></div>
  <div class="hd" style="left:426px">Power V/50Hz</div>
  <div class="hd" style="left:519px">$</div>

  <div class="group" style="top:90px">
    <div class="code r1">RTH 062 S</div><div class="code-rule"></div><div class="code r2">RTH 072 S</div>
    <div class="ver">Elettromeccanica<br>senza umidificatore<br><span>Electromechanical<br>without humidity</span></div>
    <div class="cap r1"><b>6</b> GN 2/1</div><div class="cap r2"><b>7</b> GN 2/1</div>
    <div class="sep" style="left:227px"></div>
    <div class="step r1">3.6 inch <svg width="14" height="20"><path d="M7 1V19M3 5L7 1L11 5M3 15L7 19L11 15" stroke="#333" fill="none"/></svg></div>
    <div class="step r2">3 inch <svg width="14" height="20"><path d="M7 1V19M3 5L7 1L11 5M3 15L7 19L11 15" stroke="#333" fill="none"/></svg></div>
    <div class="sep" style="left:296px"></div>
    <div class="mid dims">34.4x34x35.8 h</div>
    <div class="sep" style="left:376px"></div>
    <div class="mid wt">88 Kg</div>
    <div class="sep" style="left:420px"></div>
    <div class="mid pw">kW 12,5 3N AC 400V</div>
    <div class="sep" style="left:513px"></div>
    <div class="mid price">5,998.50</div>
  </div>

  <div class="group" style="top:162px">
    <div class="code r1">RTH 062 M</div><div class="code-rule"></div><div class="code r2">RTH 072 M</div>
    <div class="ver">Elettromeccanica<br>con umidificatore<br><span>Electromechanical<br>with humidity</span></div>
    <div class="cap r1"><b>6</b> GN 2/1</div><div class="cap r2"><b>7</b> GN 2/1</div>
    <div class="sep" style="left:227px"></div>
    <div class="step r1">3.6 inch <svg width="14" height="20"><path d="M7 1V19M3 5L7 1L11 5M3 15L7 19L11 15" stroke="#333" fill="none"/></svg></div>
    <div class="step r2">3 inch <svg width="14" height="20"><path d="M7 1V19M3 5L7 1L11 5M3 15L7 19L11 15" stroke="#333" fill="none"/></svg></div>
    <div class="sep" style="left:296px"></div>
    <div class="mid dims">34.4x34x35.8 h</div>
    <div class="sep" style="left:376px"></div>
    <div class="mid wt">88 Kg</div>
    <div class="sep" style="left:420px"></div>
    <div class="mid pw">kW 12,5 3N AC 400V</div>
    <div class="sep" style="left:513px"></div>
    <div class="mid price">6,510.00</div>
  </div>

  <div class="group" style="top:234px">
    <div class="code r1">RTH 062 E</div><div class="code-rule"></div><div class="code r2">RTH 072 E</div>
    <div class="ver">Elettronica con<br>umidificatore<br><span>Electronic with<br>humidity</span></div>
    <div class="cap r1"><b>6</b> GN 2/1</div><div class="cap r2"><b>7</b> GN 2/1</div>
    <div class="sep" style="left:227px"></div>
    <div class="step r1">3.6 inch <svg width="14" height="20"><path d="M7 1V19M3 5L7 1L11 5M3 15L7 19L11 15" stroke="#333" fill="none"/></svg></div>
    <div class="step r2">3 inch <svg width="14" height="20"><path d="M7 1V19M3 5L7 1L11 5M3 15L7 19L11 15" stroke="#333" fill="none"/></svg></div>
    <div class="sep" style="left:296px"></div>
    <div class="mid dims">34.4x34x35.8 h</div>
    <div class="sep" style="left:376px"></div>
    <div class="mid wt">88 Kg</div>
    <div class="sep" style="left:420px"></div>
    <div class="mid pw">kW 12,5 3N AC 400V</div>
    <div class="sep" style="left:513px"></div>
    <div class="mid price">7,440.00</div>
  </div>

  <p class="note" style="top:315px">Completo di paratie portateglie GN 2/1<span>Supplied with guide rails GN 2/1</span></p>
  <p class="note" style="top:351px">Possibilità sostituzione paratie portateglie con struttura estraibile e carrello, vedi pag. 28<span>Possibility to replace the guide rails for oven rack and trolley, see on page 28</span></p>

  <div class="acc" style="top:402px">
    <div class="code">BSE 021</div>
    <div class="ver">Supporto base<br><span>Support base</span></div>
    <div class="mid dims">34x30.36x33.6 h</div>
    <div class="mid wt">10 Kg</div>
    <div class="mid price">550.25</div>
  </div>
</section>

<!-- Section 2 -->
<div class="photo" style="left:48px;top:712px;width:130px;height:156px" role="img" aria-label="Photo of the 082-102 electronic holding oven"></div>
<div class="caption" style="left:48px;top:888px">RTH 082-102 E</div>
<div class="stand" style="left:45px;top:1034px;width:76px;height:98px" role="img" aria-label="Line drawing of the support base"></div>
<div class="caption" style="left:48px;top:1134px">BSE 021</div>

<section class="section" style="top:632px">
  <h2 class="s-title"><b>RTH</b> 082 - 102</h2>
  <div class="s-bar"></div>
  <div class="hd" style="left:4px">Codice<span>Code</span></div>
  <div class="hd" style="left:66px">Versione<span>Version</span></div>
  <div class="hd" style="left:157px">Capacità<span>Capacity</span></div>
  <div class="hd" style="left:231px">Passo guide<span>Distance guides</span></div>
  <div class="hd" style="left:300px">Dimensioni inch<span>Dimensions inch</span></div>
  <div class="hd" style="left:381px">Peso<span>Weight</span></div>
  <div class="hd" style="left:426px">Power V/50Hz</div>
  <div class="hd" style="left:519px">$</div>

  <div class="group" style="top:89px">
    <div class="code r1">RTH 082 S</div><div class="code-rule"></div><div class="code r2">RTH 102 S</div>
    <div class="ver">Elettromeccanica<br>senza umidificatore<br><span>Electromechanical<br>without humidity</span></div>
    <div class="cap r1"><b>8</b> GN 2/1</div><div class="cap r2"><b>10</b> GN 2/1</div>
    <div class="sep" style="left:227px"></div>
    <div class="step r1">3.6 inch <svg width="14" height="20"><path d="M7 1V19M3 5L7 1L11 5M3 15L7 19L11 15" stroke="#333" fill="none"/></svg></div>
    <div class="step r2">3 inch <svg width="14" height="20"><path d="M7 1V19M3 5L7 1L11 5M3 15L7 19L11 15" stroke="#333" fill="none"/></svg></div>
    <div class="sep" style="left:296px"></div>
    <div class="mid dims">34.4x34x44.6 h</div>
    <div class="sep" style="left:376px"></div>
    <div class="mid wt">102 Kg</div>
    <div class="sep" style="left:420px"></div>
    <div class="mid pw">kW 16 3N AC 400V</div>
    <div class="sep" style="left:513px"></div>
    <div class="mid price">7,006.00</div>
  </div>

  <div class="group" style="top:161px">
    <div class="code r1">RTH 082 M</div><div class="code-rule"></div><div class="code r2">RTH 102 M</div>
    <div class="ver">Elettromeccanica<br>con umidificatore<br><span>Electromechanical<br>with humidity</span></div>
    <div class="cap r1"><b>8</b> GN 2/1</div><div class="cap r2"><b>10</b> GN 2/1</div>
    <div class="sep" style="left:227px"></div>
    <div class="step r1">3.6 inch <svg width="14" height="20"><path d="M7 1V19M3 5L7 1L11 5M3 15L7 19L11 15" stroke="#333" fill="none"/></svg></div>
    <div class="step r2">3 inch <svg width="14" height="20"><path d="M7 1V19M3 5L7 1L11 5M3 15L7 19L11 15" stroke="#333" fill="none"/></svg></div>
    <div class="sep" style="left:296px"></div>
    <div class="mid dims">34.4x34x44.6 h</div>
    <div class="sep" style="left:376px"></div>
    <div class="mid wt">102 Kg</div>
    <div class="sep" style="left:420px"></div>
    <div class="mid pw">kW 16 3N AC 400V</div>
    <div class="sep" style="left:513px"></div>
    <div class="mid price">7,517.50</div>
  </div>

  <div class="group" style="top:233px">
    <div class="code r1">RTH 082 E</div><div class="code-rule"></div><div class="code r2">RTH 102 E</div>
    <div class="ver">Elettronica con<br>umidificatore<br><span>Electronic with<br>humidity</span></div>
    <div class="cap r1"><b>8</b> GN 2/1</div><div class="cap r2"><b>10</b> GN 2/1</div>
    <div class="sep" style="left:227px"></div>
    <div class="step r1">3.6 inch <svg width="14" height="20"><path d="M7 1V19M3 5L7 1L11 5M3 15L7 19L11 15" stroke="#333" fill="none"/></svg></div>
    <div class="step r2">3 inch <svg width="14" height="20"><path d="M7 1V19M3 5L7 1L11 5M3 15L7 19L11 15" stroke="#333" fill="none"/></svg></div>
    <div class="sep" style="left:296px"></div>
    <div class="mid dims">34.4x34x44.6 h</div>
    <div class="sep" style="left:376px"></div>
    <div class="mid wt">102 Kg</div>
    <div class="sep" style="left:420px"></div>
    <div class="mid pw">kW 16 3N AC 400V</div>
    <div class="sep" style="left:513px"></div>
    <div class="mid price">8,447.50</div>
  </div>

  <p class="note" style="top:317px">Completo di paratie portateglie GN 1/1<span>Supplied with guide rails GN 1/1</span></p>
  <p class="note" style="top:352px">Possibilità sostituzione paratie portateglie con struttura estraibile e carrello, vedi pag. 28<span>Possibility to replace the guide rails for oven rack and trolley, see on page 28</span></p>

  <div class="acc" style="top:404px">
    <div class="code">BSE 021</div>
    <div class="ver">Supporto base<br><span>Support base</span></div>
    <div class="mid dims">34x30.36x33.6 h</div>
    <div class="mid wt">10 Kg</div>
    <div class="mid price">550.25</div>
  </div>
</section>

<div class="foot-rule"></div>
<div class="folio">27</div>
</body>
</html>
```